Banner Design for Physiotherapy Business

I need a banner designed for a physiotherapy business. The word ‘Physiotherapy’ should be prominent at the top. I’ve attached a document outlining what text and a suggestion of a picture I’d like included. The photo I have suggested in the document won’t upload to plumvista though as the dimensions are too large. I am open to other photos being used though. I would like to see designs that use the colour orange (as seen in the example) or green preferrably. The dimensions need to be 841mm x 2055mm and provided in PDF, JPG, and PNG format and 300dpi in CMYK colour mode.

```html
<!DOCTYPE html>
<html lang="en">
<head>
<meta charset="utf-8">
<title>Physiotherapy Banner</title>
<link rel="stylesheet" href="https://fonts.googleapis.com/css2?family=Lato:wght@400;700;900&display=swap">
<style>
  :root {
    --orange: #e8720c;
    --amber: #f7a823;
    --yellow: #fdd33a;
    --yellow-pale: #fde680;
    --white: #ffffff;
    --blue: #1f73b7;
    --grey-text: #555555;
  }
  * { margin: 0; padding: 0; box-sizing: border-box; }
  html, body { width: 1200px; height: 2942px; overflow: hidden; background: var(--white); }
  body { font-family: "Lato", Arial, sans-serif; }
  .banner { position: relative; width: 1200px; height: 2942px; background: var(--white); overflow: hidden; }

  .top-band { position: absolute; left: 0; top: 0; width: 1200px; height: 170px; }
  .top-band .stripe-yellow { position: absolute; left: 0; top: 0; width: 100%; height: 64px; background: var(--yellow); }
  .top-band .stripe-amber { position: absolute; left: 0; top: 64px; width: 100%; height: 62px; background: var(--amber); }
  .top-band .stripe-orange { position: absolute; left: 0; top: 126px; width: 100%; height: 44px; background: var(--orange); }

  .title-bar { position: absolute; left: 0; top: 170px; width: 1200px; height: 192px; background: var(--white);
    display: flex; align-items: center; justify-content: center; }
  .title { color: var(--orange); font-weight: 400; font-size: 126px; letter-spacing: 1px; line-height: 1; }

  .hero-photo { position: absolute; left: 0; top: 362px; width: 1200px; height: 1100px;
    background: linear-gradient(160deg, #f4f1ec 0%, #e9e4dc 35%, #c9b9a4 60%, #f2efea 100%); }

  .swoosh { position: absolute; left: 0; top: 1150px; width: 1200px; height: 360px; }

  .services { position: absolute; left: 0; top: 1380px; width: 1200px; height: 1262px; background: var(--orange); }
  .services-heading { position: absolute; left: 165px; top: 122px; width: 822px; color: var(--white);
    font-weight: 700; font-size: 47px; line-height: 1; text-align: center; padding-bottom: 10px;
    border-bottom: 3px solid var(--white); }
  .service-list { position: absolute; left: 145px; top: 200px; list-style: none; color: var(--white); }
  .service-list li { position: relative; font-weight: 700; font-size: 42px; line-height: 70.8px; padding-left: 28px; }
  .service-list li::before { content: ""; position: absolute; left: 0; top: 30px; width: 12px; height: 12px;
    border-radius: 50%; background: var(--white); }
  .service-list .note { display: block; font-size: 34px; line-height: 42px; margin-top: -8px; margin-bottom: 14px; }

  .footer { position: absolute; left: 0; top: 2642px; width: 1200px; height: 208px; background: var(--white); }
  .member { position: absolute; left: 52px; top: 30px; display: flex; align-items: center; }
  .member-dot { width: 150px; height: 150px; border-radius: 50%; background: var(--blue); }
  .member-text { margin-left: 28px; color: var(--blue); }
  .member-name { font-weight: 400; font-size: 29px; line-height: 31px; width: 230px; text-transform: uppercase;
    padding-bottom: 8px; border-bottom: 2px solid var(--blue); }
  .member-label { font-size: 36px; margin-top: 6px; color: var(--grey-text); }

  .appointment { position: absolute; left: 644px; top: 8px; width: 520px; }
  .appointment-heading { color: var(--orange); font-weight: 700; font-size: 39px; line-height: 1;
    padding-bottom: 7px; border-bottom: 3px solid var(--orange); }
  .clinic, .address { color: var(--orange); font-weight: 700; font-size: 29px; line-height: 36px; }
  .clinic { margin-top: 8px; }
  .phone { display: flex; align-items: center; color: var(--orange); font-weight: 900; font-size: 39px; line-height: 46px; }
  .phone svg { width: 34px; height: 34px; margin-right: 18px; }

  .bottom-band { position: absolute; left: 0; top: 2850px; width: 1200px; height: 92px; }
  .bottom-band .stripe-yellow { position: absolute; left: 0; top: 0; width: 100%; height: 30px; background: var(--yellow); }
  .bottom-band .stripe-amber { position: absolute; left: 0; top: 30px; width: 100%; height: 32px; background: var(--amber); }
  .bottom-band .stripe-orange { position: absolute; left: 0; top: 62px; width: 100%; height: 30px; background: var(--orange); }
</style>
</head>
<body>
<div class="banner">
  <div class="top-band">
    <div class="stripe-yellow"></div>
    <div class="stripe-amber"></div>
    <div class="stripe-orange"></div>
  </div>

  <header class="title-bar">
    <h1 class="title">PHYSIOTHERAPY</h1>
  </header>

  <div class="hero-photo" role="img" aria-label="Physiotherapist treating a patient's shoulder on a treatment table in a bright clinic room"></div>

  <svg class="swoosh" viewBox="0 0 1200 360" preserveAspectRatio="none" aria-hidden="true">
    <path d="M0 150 C 300 330, 800 300, 1200 40 L1200 360 L0 360 Z" fill="var(--yellow-pale)"/>
    <path d="M0 175 C 320 345, 820 320, 1200 90 L1200 360 L0 360 Z" fill="var(--yellow)"/>
    <path d="M0 205 C 340 355, 840 345, 1200 150 L1200 360 L0 360 Z" fill="var(--amber)"/>
    <path d="M0 232 C 360 360, 860 360, 1200 210 L1200 360 L0 360 Z" fill="var(--orange)"/>
  </svg>

  <section class="services">
    <h2 class="services-heading">WHAT WE TREAT / SERVICES</h2>
    <ul class="service-list">
      <li>Arthritis</li>
      <li>Back pain / Neck pain</li>
      <li>Sciatic pain</li>
      <li>Sports injuries</li>
      <li>Repetitive strain injuries</li>
      <li>Post surgical management<span class="note">(hip and knee arthroscopes, joint replacement surgery)</span></li>
      <li>Shoulder pain and dysfunction</li>
      <li>Tennis elbow</li>
      <li>Postural pain</li>
      <li>Workplace injuries</li>
      <li>Motor vehicle accidents</li>
      <li>Women's health issues</li>
      <li>Clinical exercise</li>
      <li>Pre-employment functional assessments</li>
    </ul>
  </section>

  <footer class="footer">
    <div class="member">
      <div class="member-dot"></div>
      <div class="member-text">
        <div class="member-name">Allied Physio Network</div>
        <div class="member-label">Member</div>
      </div>
    </div>
    <div class="appointment">
      <div class="appointment-heading">MAKE AN APPOINTMENT</div>
      <div class="clinic">Kestrel Family Practice</div>
      <div class="address">18-20 Harlow St Kestrel VIC 3199</div>
      <div class="phone">
        <svg viewBox="0 0 24 24" aria-hidden="true">
          <circle cx="12" cy="12" r="10.5" fill="none" stroke="var(--orange)" stroke-width="2"/>
          <path d="M8.6 6.8 L10.4 6.6 L11.2 9.2 L10 10.2 C10.6 11.8 11.9 13.2 13.6 13.9 L14.6 12.7 L17.2 13.5 L17 15.4 C13 16.2 7.6 11 8.6 6.8 Z" fill="var(--orange)"/>
        </svg>
        (03) 5550 0142
      </div>
    </div>
  </footer>

  <div class="bottom-band">
    <div class="stripe-yellow"></div>
    <div class="stripe-amber"></div>
    <div class="stripe-orange"></div>
  </div>
</div>
</body>
</html>
```